Web Pages Improvement, Update of existing BRUN website

Redesign existing website www.brun.asn.au The # of pages can be reduced to a total of 6 including the home page. We have a design project out for the logo for this site so feel free to bid for that also.
As this is a simple brief with basic pages, we expect the end result to be code ready for uploaded to our existing host.

```html
<!DOCTYPE html>
<html lang="en">
<head>
<meta charset="utf-8">
<title>BRUN – Home</title>
<link rel="stylesheet" href="https://fonts.googleapis.com/css2?family=Open+Sans:wght@400;600;700&family=PT+Sans:wght@400;700&family=Noto+Serif:wght@700&display=swap">
<style>
  :root {
    --orange: #f07d0a;
    --orange-light: #f9a640;
    --orange-dark: #d8660a;
    --heading-orange: #d9650c;
    --page-top: #efefef;
    --band: #6b6b6b;
    --nav-border: #d4d4d4;
    --text: #444;
    --text-dark: #222;
    --white: #fff;
    --rule: #d0d0d0;
  }
  * { margin: 0; padding: 0; box-sizing: border-box; }
  html, body { width: 1145px; height: 1200px; overflow: hidden; }
  body {
    position: relative;
    background: linear-gradient(var(--page-top) 0, var(--page-top) 498px, var(--white) 498px);
    font-family: "Open Sans", sans-serif;
    color: var(--text);
  }
  .abs { position: absolute; }
  h1, h2 { font-weight: 400; }

  /* header */
  .brand { left: 44px; top: 40px; display: flex; align-items: center; gap: 12px; font-family: "Open Sans", sans-serif; font-weight: 600; font-size: 34px; line-height: 1; color: var(--text-dark); }
  .brand-square { width: 30px; height: 30px; background: var(--orange); }
  .header-email { left: 912px; top: 32px; font-size: 16px; color: #444; }
  .search { left: 885px; top: 68px; width: 212px; height: 28px; border: 1px solid #cfcfcf; border-radius: 14px; background: var(--white); box-shadow: inset 0 1px 3px rgba(0,0,0,.12); }
  .search span { position: absolute; left: 20px; top: 5px; font-size: 12px; font-style: italic; color: #888; }
  .search svg { position: absolute; right: 12px; top: 7px; }

  /* slider */
  .slider { left: 136px; top: 132px; width: 872px; height: 316px; background: linear-gradient(90deg,#f6f6f6,#e4e4e4 6%,#e4e4e4 94%,#f6f6f6); box-shadow: 0 14px 14px -8px rgba(0,0,0,.45); }
  .slide-photo { left: 49px; top: 0; width: 774px; height: 316px; background: linear-gradient(100deg,#d8d8d8 0%,#c4c4c4 40%,#b9b9b9 100%); }
  .slide-caption { left: 449px; top: 92px; width: 360px; font-family: "Noto Serif", serif; font-weight: 700; font-size: 17px; line-height: 27px; color: #333; }
  .slide-button { left: 674px; top: 157px; width: 93px; height: 27px; border-radius: 14px; background: #1b1b1b; color: #ccc; font-family: "Noto Serif", serif; font-size: 12px; text-align: center; line-height: 27px; }
  .slide-arrow { top: 138px; }

  /* nav */
  .band { left: 0; top: 498px; width: 1145px; height: 29px; background: var(--band); }
  .nav { left: 40px; top: 485px; width: 1066px; height: 58px; display: flex; list-style: none; background: linear-gradient(#f7f7f7,#e6e6e6); border: 1px solid var(--nav-border); box-shadow: 0 2px 3px rgba(0,0,0,.15); }
  .nav li { height: 100%; display: flex; align-items: center; justify-content: center; font-size: 16px; color: #444; border-right: 1px solid var(--nav-border); }
  .nav li:last-child { border-right: 0; }
  .nav .active { background: linear-gradient(var(--orange-light),var(--orange)); color: #2b2b2b; }

  /* content */
  .welcome { left: 44px; top: 572px; font-size: 23px; color: var(--heading-orange); }
  .intro { left: 44px; top: 616px; width: 642px; font-family: "PT Sans", sans-serif; font-size: 12.4px; line-height: 21.8px; color: #444; text-align: justify; }
  .intro p { margin-bottom: 2px; }
  .intro p.gap { margin-top: 12px; }
  .marks { left: 220px; top: 1022px; display: flex; gap: 32px; align-items: center; }
  .mark { width: 30px; height: 30px; background: #111; }
  .mark.round { border-radius: 50%; }

  /* member listing */
  .listing { left: 725px; top: 562px; width: 373px; height: 296px; border-radius: 4px; background: linear-gradient(var(--orange-light),var(--orange) 60%,var(--orange-dark)); box-shadow: 0 2px 3px rgba(0,0,0,.2); }
  .listing h2 { position: absolute; left: 12px; top: 14px; font-size: 18px; color: #1f1f1f; }
  .listing .states { position: absolute; left: 13px; top: 52px; font-size: 12.5px; color: #1f1f1f; }
  .listing .updown { position: absolute; right: 22px; top: 16px; }
  .listing-card { position: absolute; left: 11px; top: 85px; width: 351px; height: 199px; background: var(--white); border-radius: 4px; padding: 14px 14px; font-size: 13px; color: #222; line-height: 19.5px; }
  .listing-card .org { margin-bottom: 6px; }
  .listing-card .addr { color: #555; }
  .listing-card table { margin-top: 8px; border-collapse: collapse; font-size: 13px; color: #222; }
  .listing-card td { padding: 0 8px 0 2px; line-height: 19.5px; }

  /* links */
  .links-head { left: 725px; top: 873px; width: 371px; height: 28px; background: #e9e9e9; font-size: 18px; color: var(--heading-orange); padding: 1px 13px; }
  .links-tabs { left: 736px; top: 910px; font-size: 12.5px; color: #222; }
  .links-tabs .current { color: var(--heading-orange); border-bottom: 1px solid #888; padding-bottom: 2px; }
  .links-list { left: 736px; top: 945px; width: 340px; list-style: none; font-size: 13px; color: #555; }
  .links-list li { line-height: 15px; margin-bottom: 11px; }
  .scroll-track { left: 1086px; top: 913px; width: 3px; height: 160px; background: #aaa; }
  .scroll-knob { left: 1079px; top: 930px; width: 17px; height: 17px; border-radius: 50%; background: var(--orange); border: 2px solid #f3c48d; }

  /* footer */
  .footer-rule { left: 40px; top: 1102px; width: 1066px; height: 3px; background: var(--rule); }
  .copyright { left: 40px; top: 1139px; font-family: "PT Sans", sans-serif; font-size: 12px; color: #333; }
  .social { left: 904px; top: 1135px; display: flex; gap: 18px; list-style: none; }
  .social li { width: 25px; height: 25px; border-radius: 2px; box-shadow: 1px 2px 2px rgba(0,0,0,.3); }
</style>
</head>
<body>
  <header>
    <div class="abs brand"><span class="brand-square"></span>BRUN</div>
    <div class="abs header-email">Email : info@brun.com</div>
    <div class="abs search">
      <span>Search</span>
      <svg width="16" height="14" viewBox="0 0 16 14"><circle cx="6" cy="6" r="4.5" fill="none" stroke="#999" stroke-width="1.6"/><line x1="9.5" y1="9" x2="14" y2="12.5" stroke="#999" stroke-width="2.2" stroke-linecap="round"/></svg>
    </div>
  </header>

  <section class="abs slider">
    <div class="abs slide-photo" role="img" aria-label="Hands testing a plug with a red screwdriver"></div>
    <p class="abs slide-caption">Excepteur sint occaecat cupidatat non proident, sunt in culpa qui</p>
    <div class="abs slide-button">View more</div>
    <svg class="abs slide-arrow" style="left:16px" width="18" height="28" viewBox="0 0 18 28"><polyline points="15,3 4,14 15,25" fill="none" stroke="#555" stroke-width="3.5"/></svg>
    <svg class="abs slide-arrow" style="left:838px" width="18" height="28" viewBox="0 0 18 28"><polyline points="3,3 14,14 3,25" fill="none" stroke="#555" stroke-width="3.5"/></svg>
  </section>

  <div class="abs band"></div>
  <ul class="abs nav">
    <li class="active" style="width:122px">Home</li>
    <li style="width:216px">Statement of Purpose</li>
    <li style="width:174px">Types of Testing</li>
    <li style="width:171px">Member Listing</li>
    <li style="width:123px">Members</li>
    <li style="width:142px">Contact Us</li>
    <li style="width:118px">Links</li>
  </ul>

  <main>
    <h1 class="abs welcome">Welcome to our site</h1>
    <div class="abs intro">
      <p>The Bureau of Regulated Utility Networks of Australia (BRUN) was established in 1995 to foster the growth of a professional and value adding compliance testing resource to serve the needs of Australian industry.</p>
      <p>BRUN is an incorporated association formed by NBTL accredited electrical testing laboratories in Australia and includes an accredited member from New Zealand. The association has 14 active members which operate laboratories in a total of 18 locations in Australia and New Zealand. The members provide testing services to the public in the areas of electrical safety, electromagnetic compatibility, electromagnetic radiation, electromedical equipment, energy efficiency labelling, environmental performance, gas appliances, lighting equipment, performance ratings, and telecommunications. The NBTL accreditation mark is shown below.</p>
      <p class="gap">The Association operates a paid secretariat to service the interests of its members and to provide information about the services available to the public from its members. The registered office is in Harlow, Victoria. The members of BRUN meet regularly to discuss issues of interest to its members and the testing industry and to make submissions to regulators, public investigations, inquiries and industry surveys. The Association nominates members to serve on relevant Committees of Standards Council and to make representations to government inquiries.</p>
      <p class="gap">Member laboratories of BRUN test equipment to Australian and International Standards so that the clients are able to apply the appropriate regulatory mark for their product. The commonly recognised regulatory marks are the R-Mark and S-Mark for Australia, EU Mark for Europe, US Mark for the USA as shown below.</p>
    </div>
    <div class="abs marks" aria-label="Accreditation and regulatory marks">
      <span class="mark"></span>
      <span class="mark round"></span>
      <span class="mark"></span>
      <span class="mark round"></span>
      <span class="mark"></span>
    </div>
  </main>

  <aside>
    <section class="abs listing">
      <h2>Member Listing</h2>
      <div class="states">NSW &nbsp;|&nbsp; VIC &nbsp;|&nbsp; QLD &nbsp;|&nbsp; SA &nbsp;|&nbsp; NZ</div>
      <svg class="updown" width="28" height="50" viewBox="0 0 28 50"><polyline points="3,14 14,4 25,14" fill="none" stroke="#fff" stroke-width="3"/><polyline points="3,36 14,46 25,36" fill="none" stroke="#fff" stroke-width="3"/></svg>
      <div class="listing-card">
        <div class="org">Bureau of Regulated Utility Networks</div>
        <div>BRUN Secretariat</div>
        <div class="addr">48 Harlow Street,<br>Harlow Vic. 3099</div>
        <table>
          <tr><td>Email:</td><td>secretariat@brun.com.au</td></tr>
          <tr><td>Telephone:</td><td>+61 (0)3 9000 4812</td></tr>
          <tr><td>Facsimile:</td><td>+61 (0)3 9000 4813</td></tr>
          <tr><td>Mobile:</td><td>+61 (0)400 555 217</td></tr>
        </table>
      </div>
    </section>

    <h2 class="abs links-head">Links</h2>
    <div class="abs links-tabs"><span class="current">Australia</span> &nbsp; | &nbsp; Overseas</div>
    <ul class="abs links-list">
      <li>National Board of Test Laboratories, Australia</li>
      <li>Federal Signal and Media Council</li>
      <li>Standards Council</li>
      <li>Radiation Safety and Shielding Office<br>(RSSO)</li>
    </ul>
    <div class="abs scroll-track"></div>
    <div class="abs scroll-knob"></div>
  </aside>

  <footer>
    <div class="abs footer-rule"></div>
    <p class="abs copyright">Copyright © 2012 www.brun.com &nbsp;&nbsp;All rights reserved</p>
    <ul class="abs social" aria-label="Social links">
      <li style="background:#3b5a99"></li>
      <li style="background:#5cbbe6"></li>
      <li style="background:#f0711e"></li>
      <li style="background:#1f6fa8"></li>
      <li style="background:#4aa04a"></li>
    </ul>
  </footer>
</body>
</html>
```